Modernize Cleaning Chemical Product Labels

I am looking to modernise our product labels.
We are a cleaning chemical manufacture predominately in the commercial cleaning industry.
I would like for the labels to be available in at least 6 colours, red, green, blue, yellow, purple and orange.
Design can be as small as 270mm x 140mm up to 340mm x 165mm. Current label dimensions 275mm x 165mm
I have attached some of our current labels and our logo and also some competitors labels

Colors
0054AA
0677BA
7BADD7
CADEEF
E8F1F8
00AB8E
00BBA5
67D7C9
C6EFE9
E9F9F6
FFF300
FFF600
FEFA6F
FFFEC7
FFFEE8
F0912C
F2A743
F7CA91
FBE8D2
FDF5EE
EB3D1F
EC4F4E
F09395
F8D3D4
FCEDEE
A7469A
B969AE
D3A5CF
EDDBEB
F8F0F9

```html
<!DOCTYPE html>
<html lang="en">
<head>
<meta charset="utf-8">
<title>Brightline Premium Dishwashing Detergent – Label Colourways</title>
<link href="https://fonts.googleapis.com/css2?family=Fira+Sans:wght@400;600;700;800&family=Open+Sans:wght@400;600&display=swap" rel="stylesheet">
<style>
  :root {
    --page: #ffffff;
    --label-bg-a: #f4f4f4;
    --label-bg-b: #e2e2e2;
    --white: #ffffff;
    --purple: #4a1fa3;
    --green: #3dbf0a;
    --yellow-frame: #e6c545;
    --red-frame: #e0463a;
    --icon-fill: #d9d9de;
  }
  * { box-sizing: border-box; margin: 0; padding: 0; }
  html, body { width: 1200px; height: 1015px; overflow: hidden; background: var(--page); }
  .canvas {
    position: relative; width: 1200px; height: 1015px;
    display: flex; justify-content: center; align-items: center; gap: 40px;
  }
  .label {
    position: relative; width: 560px; height: 491px; overflow: hidden;
    background: linear-gradient(135deg, var(--label-bg-a) 0%, var(--white) 35%, var(--label-bg-b) 60%, var(--white) 85%, var(--label-bg-a) 100%);
    font-family: "Open Sans", sans-serif;
    color: var(--accent);
  }
  .label--purple { --accent: var(--purple); --frame: var(--yellow-frame); }
  .label--green { --accent: var(--green); --frame: var(--red-frame); }

  .label__band { position: absolute; left: 0; top: 0; width: 100%; height: 22px; background: var(--accent); }

  .hazard { position: absolute; left: 6px; top: 26px; display: flex; gap: 6px; align-items: flex-start; }
  .hazard__pictogram { width: 18px; height: 44px; background: var(--accent); border-radius: 9px 9px 3px 3px; }
  .hazard__text { font-family: "Fira Sans", sans-serif; font-weight: 700; font-size: 8px; line-height: 1.25; padding-top: 2px; }

  .brand {
    position: absolute; left: 290px; top: 26px; width: 160px; text-align: center;
    font-family: "Fira Sans", sans-serif; font-weight: 800; font-size: 24px; letter-spacing: 1px;
    color: var(--accent);
  }

  .warning { position: absolute; left: 235px; top: 116px; font-family: "Fira Sans", sans-serif; }
  .warning__title { font-weight: 700; font-size: 12px; margin-bottom: 4px; }
  .warning__line { font-size: 6.2px; line-height: 1.3; text-transform: uppercase; }

  .product__rule { position: absolute; left: 221px; top: 172px; width: 295px; height: 4px; background: var(--accent); }
  .product__name {
    position: absolute; left: 235px; top: 176px;
    font-family: "Fira Sans", sans-serif; font-weight: 800; font-size: 37px; line-height: 1; letter-spacing: 0.5px;
  }
  .product__panel {
    position: absolute; left: 221px; top: 217px; width: 295px; height: 209px;
    background: var(--accent); color: var(--white); font-family: "Fira Sans", sans-serif;
  }
  .product__type { position: absolute; left: 12px; top: 10px; font-weight: 800; font-size: 20px; line-height: 1.1; letter-spacing: 0.6px; }
  .product__claim { position: absolute; left: 12px; top: 92px; font-weight: 800; font-size: 14px; letter-spacing: 0.6px; }
  .product__features { position: absolute; left: 12px; top: 121px; list-style: none; font-weight: 600; font-size: 11px; line-height: 15.5px; }
  .product__maker { position: absolute; left: 194px; top: 130px; border-left: 1px solid var(--white); padding-left: 5px; font-size: 6px; line-height: 1.5; }
  .product__volume { position: absolute; left: 237px; top: 172px; font-weight: 700; font-size: 23px; }

  .uses__icons {
    position: absolute; left: 28px; top: 221px; width: 183px; height: 36px;
    border: 1px solid var(--frame); background: var(--white); padding: 6px;
  }
  .uses__icons-fill { width: 100%; height: 100%; background: linear-gradient(90deg, var(--icon-fill), var(--accent) 50%, var(--icon-fill)); opacity: 0.55; }

  .info { position: absolute; left: 34px; top: 269px; width: 175px; font-size: 6.6px; line-height: 1.4; }
  .info p { margin-bottom: 6px; }
  .info__justify { text-align: justify; }
  .info__heading { font-weight: 600; text-transform: uppercase; margin-bottom: 2px; }
</style>
</head>
<body>
<main class="canvas">

  <section class="label label--purple" aria-label="Purple label">
    <div class="label__band"></div>
    <div class="hazard">
      <div class="hazard__pictogram" role="img" aria-label="Health hazard pictogram of a standing figure"></div>
      <p class="hazard__text">Causes skin irritation.<br>May cause an allergic skin reaction.</p>
    </div>
    <div class="brand">HARTWELL</div>
    <div class="warning">
      <p class="warning__title">WARNING</p>
      <p class="warning__line">Not to be taken</p>
      <p class="warning__line">Keep out of reach of children</p>
      <p class="warning__line">Read safety directions before opening</p>
    </div>
    <div class="product__rule"></div>
    <h1 class="product__name">BRIGHTLINE</h1>
    <div class="product__panel">
      <p class="product__type">PREMIUM<br>DISHWASHING<br>DETERGENT</p>
      <p class="product__claim">BIODEGRADABLE</p>
      <ul class="product__features">
        <li>High Solids Content</li>
        <li>Only 5 to 10mLs per 10L Wash</li>
        <li>Grease and Oil Cutters + y</li>
        <li>Coconut Oil Derivatives</li>
        <li>Lemon Scented</li>
      </ul>
      <p class="product__maker">Hartwell Chemical Products<br>12 Bayview Park Rd.,<br>Marlow 4021. (07) 5550 1234</p>
      <p class="product__volume">5 L</p>
    </div>
    <div class="uses__icons"><div class="uses__icons-fill" role="img" aria-label="Row of use icons: dishes, tiles, kitchen, walls, floors, bathroom, painted surfaces"></div></div>
    <div class="info">
      <p>USES: Hand dishwashing, floors, kitchens, walls, tiles, bathroom and all painted surfaces.</p>
      <p class="info__justify">This product is a highly efficient, bio-degradable liquid detergent with a neutral pH, designed to achieve optimum results on a cost performance basis. It is a unique blend of ionic and non-ionic surfactants coupled with coconut oil derivatives to produce a high solids detergent with excellent streak-free rinsing properties.</p>
      <p>APPLICATIONS: Hand dishwashing, floors, walls, benches, cars, house- washing (interior and exterior) and hand washing of fine fabrics</p>
      <p class="info__heading">Dilutions</p>
      <p>5 - 10ml per 10 Litres for dishwashing (1:1000)<br>50-150ml per 10 litres for floors, walls, cars, caravans, houses etc. (5-15:1000)</p>
    </div>
  </section>

  <section class="label label--green" aria-label="Green label">
    <div class="label__band"></div>
    <div class="hazard">
      <div class="hazard__pictogram" role="img" aria-label="Health hazard pictogram of a standing figure"></div>
      <p class="hazard__text">Causes skin irritation.<br>May cause an allergic skin reaction.</p>
    </div>
    <div class="brand">HARTWELL</div>
    <div class="warning">
      <p class="warning__title">WARNING</p>
      <p class="warning__line">Not to be taken</p>
      <p class="warning__line">Keep out of reach of children</p>
      <p class="warning__line">Read safety directions before opening</p>
    </div>
    <div class="product__rule"></div>
    <h1 class="product__name">BRIGHTLINE</h1>
    <div class="product__panel">
      <p class="product__type">PREMIUM<br>DISHWASHING<br>DETERGENT</p>
      <p class="product__claim">BIODEGRADABLE</p>
      <ul class="product__features">
        <li>High Solids Content</li>
        <li>Only 5 to 10mLs per 10L Wash</li>
        <li>Grease and Oil Cutters + y</li>
        <li>Coconut Oil Derivatives</li>
        <li>Lemon Scented</li>
      </ul>
      <p class="product__maker">Hartwell Chemical Products<br>12 Bayview Park Rd.,<br>Marlow 4021. (07) 5550 1234</p>
      <p class="product__volume">5 L</p>
    </div>
    <div class="uses__icons"><div class="uses__icons-fill" role="img" aria-label="Row of use icons: dishes, tiles, kitchen, walls, floors, bathroom, painted surfaces"></div></div>
    <div class="info">
      <p>USES: Hand dishwashing, floors, kitchens, walls, tiles, bathroom and all painted surfaces.</p>
      <p class="info__justify">This product is a highly efficient, bio-degradable liquid detergent with a neutral pH, designed to achieve optimum results on a cost performance basis. It is a unique blend of ionic and non-ionic surfactants coupled with coconut oil derivatives to produce a high solids detergent with excellent streak-free rinsing properties.</p>
      <p>APPLICATIONS: Hand dishwashing, floors, walls, benches, cars, house- washing (interior and exterior) and hand washing of fine fabrics</p>
      <p class="info__heading">Dilutions</p>
      <p>5 - 10ml per 10 Litres for dishwashing (1:1000)<br>50-150ml per 10 litres for floors, walls, cars, caravans, houses etc. (5-15:1000)</p>
    </div>
  </section>

</main>
</body>
</html>
```